The Velvet Needle Poster for a shop Facade

Hello Designers,

• We have a 4X4 meters façade for our tailor shop “The Velvet Needle”, and we are looking for a unique, simple and attractive poster to be printed on the glass to attract the attention of the driving customers or whoever passes by the shop.
• The Velvet Needle, with ‘Velvet’ referring to door-to-door service, our concept as follows (Call … Measure … Stitch … Deliver)

1. Step1: Book online or simply call us to make your appointment (should be pictorial not writing)
2. Step2: Our dedicated personnel will come to you at your preferred time and location. (should be pictorial not writing)
3. Step3: Clothes Alteration/Making to suit your style and body fit. (should be pictorial not writing)
4. Step4: Delivery on completion, at your preferred time and location. (should be pictorial not writing)

• We are specialized in clothes alteration and making for both men and women, and anything related to tailoring services www.thevelvetneedle-example.com

• The poster must include the name “The Velvet Needle” as well as the phone number 04 312 8817 in a very clear and obvious way (logo will be optional if you can show it in a nice way)
And the concept of our shop should be shown in the poster in a very simple and clear way and more graphical than words. (Perhaps a graphical flow to show client booking our service and we go to their place for alterations done).
Colors should be chosen carefully to attract the customers and the walk-ins eyes when they pass by either walking or by cars.

Thank you
Rami

Target Market(s)

We have a 4X4 meters façade for our tailor shop “The Velvet Needle”, and we are looking for a unique, simple and attractive poster to be printed on the glass to attract the attention of the driving customers or whoever passes by the shop.

Industry/Entity Type

Fashion

• to match the poster/signage

Colors

Designer to choose colors to be used in the design.

Requirements
Must have
Nice to have
• the concept of our shop should be shown in the poster in a very simple and clear way and more graphical than words. (Perhaps a graphical flow to show client booking our service and we go to their place for alterations done).
Should not have
• many words, copied designs. Please only use the images attached in the project brief for reference.

```html
<!DOCTYPE html>
<html lang="en">
<head>
<meta charset="utf-8">
<title>The Velvet Needle – Facade Poster</title>
<link href="https://fonts.googleapis.com/css2?family=Montserrat:wght@300;400;500;700&display=swap" rel="stylesheet">
<style>
  :root {
    --ink-dark: #141416;
    --ink-mid: #232326;
    --ink-warm: #2e2a28;
    --paper: #f2f2f0;
    --line: #e8e8e6;
    --text-soft: #d9d9d7;
  }
  * { margin: 0; padding: 0; box-sizing: border-box; }
  html, body { width: 1200px; height: 1200px; overflow: hidden; background: var(--ink-dark); }
  .poster {
    position: relative;
    width: 1200px;
    height: 1200px;
    font-family: "Montserrat", sans-serif;
    color: var(--paper);
    overflow: hidden;
  }
  .backdrop {
    position: absolute;
    inset: 0;
    background:
      radial-gradient(ellipse 70% 45% at 45% 72%, var(--ink-warm) 0%, transparent 70%),
      linear-gradient(180deg, var(--ink-dark) 0%, var(--ink-dark) 38%, var(--ink-mid) 100%);
  }
  .artwork { position: absolute; inset: 0; }
  .brand {
    position: absolute;
    left: 0; right: 0;
    top: 196px;
    text-align: center;
  }
  .brand-name {
    font-weight: 300;
    font-size: 52px;
    letter-spacing: 1px;
    line-height: 64px;
    color: var(--paper);
  }
  .brand-tagline {
    position: absolute;
    left: 0; right: 0;
    top: 347px;
    text-align: center;
    font-weight: 300;
    font-size: 15px;
    letter-spacing: 6px;
    line-height: 20px;
    color: var(--text-soft);
  }
  .process-title {
    position: absolute;
    left: 0; right: 0;
    top: 450px;
    text-align: center;
    font-weight: 500;
    font-size: 37px;
    line-height: 46px;
    letter-spacing: 0;
  }
  .step-text {
    position: absolute;
    width: 240px;
    text-align: center;
    font-weight: 400;
    font-size: 21px;
    line-height: 31.5px;
    color: var(--paper);
  }
  .step-book    { left: 86px;  top: 712px; }
  .step-visit   { left: 347px; top: 759px; }
  .step-stitch  { left: 602px; top: 712px; }
  .step-deliver { left: 850px; top: 759px; }
  .shop-name {
    position: absolute;
    left: 0; right: 0;
    top: 1000px;
    text-align: center;
    font-weight: 400;
    font-size: 38px;
    line-height: 46px;
    letter-spacing: 0.5px;
  }
  .call-pill {
    position: absolute;
    left: 374px;
    top: 1063px;
    width: 444px;
    height: 52px;
    border-radius: 26px;
    background: var(--paper);
    color: var(--ink-dark);
    text-align: center;
    font-weight: 700;
    font-size: 38px;
    line-height: 53px;
  }
</style>
</head>
<body>
<main class="poster">
  <div class="backdrop" role="img" aria-label="Dark tailoring workbench photo with scissors, tape measure and fabric swatch cards"></div>

  <svg class="artwork" width="1200" height="1200" viewBox="0 0 1200 1200" aria-hidden="true">
    <path d="M202 474 H67 V1087 H374 M818 1087 H1124 V474 H998" fill="none" stroke="var(--line)" stroke-width="2"/>
    <path d="M83 615 C140 610 170 612 206 619 C300 640 380 600 467 655 C560 700 640 600 722 615 C820 630 880 700 970 664 C1040 630 1070 605 1108 615"
          fill="none" stroke="var(--line)" stroke-width="2.5" stroke-dasharray="3 4"/>

    <g class="step-badge">
      <circle cx="206" cy="619" r="64" fill="var(--ink-dark)" stroke="var(--line)" stroke-width="3" stroke-dasharray="5 4"/>
      <circle cx="206" cy="619" r="56" fill="var(--paper)"/>
      <path d="M186 596 l12 -4 l8 18 l-8 6 c4 10 10 16 20 20 l6 -8 l18 8 l-4 12 c-30 4 -58 -24 -52 -52z"
            fill="none" stroke="var(--ink-dark)" stroke-width="3.5" stroke-linejoin="round"/>
    </g>
    <g class="step-badge">
      <circle cx="467" cy="655" r="64" fill="var(--ink-dark)" stroke="var(--line)" stroke-width="3" stroke-dasharray="5 4"/>
      <circle cx="467" cy="655" r="56" fill="var(--paper)"/>
      <path d="M467 690 c-14 -18 -24 -30 -24 -44 a24 24 0 0 1 48 0 c0 14 -10 26 -24 44z"
            fill="none" stroke="var(--ink-dark)" stroke-width="3.5" stroke-linejoin="round"/>
      <circle cx="467" cy="645" r="8" fill="none" stroke="var(--ink-dark)" stroke-width="3.5"/>
    </g>
    <g class="step-badge">
      <circle cx="722" cy="615" r="64" fill="var(--ink-dark)" stroke="var(--line)" stroke-width="3" stroke-dasharray="5 4"/>
      <circle cx="722" cy="615" r="56" fill="var(--paper)"/>
      <path d="M698 616 l16 16 l32 -34" fill="none" stroke="var(--ink-dark)" stroke-width="4.5" stroke-linecap="round" stroke-linejoin="round"/>
    </g>
    <g class="step-badge">
      <circle cx="970" cy="664" r="64" fill="var(--ink-dark)" stroke="var(--line)" stroke-width="3" stroke-dasharray="5 4"/>
      <circle cx="970" cy="664" r="56" fill="var(--paper)"/>
      <path d="M944 664 H994 M978 648 l16 16 l-16 16" fill="none" stroke="var(--ink-dark)" stroke-width="4.5" stroke-linecap="round" stroke-linejoin="round"/>
    </g>
  </svg>

  <header class="brand">
    <p class="brand-name">The Velvet Needle</p>
  </header>
  <p class="brand-tagline">Clothes<br>Alterations</p>

  <h1 class="process-title">CALL—MEASURE—STITCH—DELIVER</h1>

  <p class="step-text step-book">Book online or simply call us to make your appointment.</p>
  <p class="step-text step-visit">Our dedicated personnel will come to you at your preferred time and location.</p>
  <p class="step-text step-stitch">Clothes Alteration / Making to suit your style and body fit.</p>
  <p class="step-text step-deliver">Delivery on completion, at your preferred time and location.</p>

  <p class="shop-name">THE VELVET NEEDLE</p>
  <p class="call-pill">CALL 04 312 8817</p>
</main>
</body>
</html>
```